ALL TYPES OF COMMERCIAL PLASTERING

TYPE OF BLOCK LETTERING WITH STAND OUT QUALITIES
WITH SOME TYPE OF LOGO
SOMETHING UNIQUE FOR THE BUILDING INDUSTRY.
QUALITY WORKMANSHIP
Updates

forgot to include my mobile phone number on my brief. could you add it to your design please MOBILE PH 0412 858 196

please let me make this quite clear ,the company name is harbourline linings and Fitouts PTY LTD. THE TYPE OF WORK WE WILL BE DOING IS COMMERCIAL PLASTERING.

Industry/Entity Type

Industry

Contact Information for Business Card

harbourline linings and fitouts P/L
marcus devlin p.o.box 42 wendouree 3355 email address harbourlinelinings@examplemail.com
ABN 51 718 294 605 COMMERCIAL PLASTERING

```html
<!DOCTYPE html>
<html lang="en">
<head>
<meta charset="utf-8">
<title>Harbourline Linings and Fitouts P/L – Business Card</title>
<link rel="stylesheet" href="https://fonts.googleapis.com/css2?family=Arimo:wght@400;700&display=swap">
<style>
  :root {
    --brand-blue: #3d4fa6;
    --card-white: #ffffff;
    --backdrop: #eceef1;
    --card-shadow: rgba(30, 35, 60, 0.18);
  }
  * { box-sizing: border-box; margin: 0; padding: 0; }
  html, body {
    width: 1200px;
    height: 864px;
    overflow: hidden;
    background: var(--backdrop);
    font-family: "Arimo", Arial, sans-serif;
  }
  .stage {
    width: 1200px;
    height: 864px;
    display: flex;
    align-items: center;
    justify-content: center;
  }
  .business-card {
    position: relative;
    width: 1000px;
    height: 572px;
    background: var(--card-white);
    box-shadow: 0 18px 40px var(--card-shadow);
    color: var(--brand-blue);
  }
  .brand {
    position: absolute;
    left: 56px;
    top: 54px;
    display: flex;
    align-items: center;
    gap: 26px;
  }
  .brand-mark {
    width: 140px;
    height: 140px;
    border-radius: 50%;
    background: var(--brand-blue);
    flex: none;
  }
  .brand-name {
    font-weight: 700;
    font-size: 40px;
    line-height: 1.12;
    letter-spacing: 1px;
    text-transform: uppercase;
  }
  .person-name {
    position: absolute;
    left: 60px;
    top: 262px;
    font-size: 36px;
    font-weight: 400;
  }
  .contact-list {
    position: absolute;
    left: 60px;
    top: 350px;
    list-style: none;
  }
  .contact-item {
    display: flex;
    align-items: center;
    gap: 22px;
    height: 44px;
    font-size: 24px;
    font-weight: 400;
  }
  .contact-icon {
    width: 22px;
    height: 22px;
    fill: var(--brand-blue);
    flex: none;
  }
</style>
</head>
<body>
<main class="stage">
  <article class="business-card">
    <header class="brand">
      <span class="brand-mark" aria-hidden="true"></span>
      <h1 class="brand-name">Harbourline Linings<br>and Fitouts P/L</h1>
    </header>

    <p class="person-name">marcus devlin</p>

    <ul class="contact-list">
      <li class="contact-item">
        <svg class="contact-icon" viewBox="0 0 24 24" aria-hidden="true">
          <path d="M7 1h10a2 2 0 0 1 2 2v18a2 2 0 0 1-2 2H7a2 2 0 0 1-2-2V3a2 2 0 0 1 2-2zm0 3v11h10V4zm3 14v2h4v-2z"/>
        </svg>
        <span>0412 858 196</span>
      </li>
      <li class="contact-item">
        <svg class="contact-icon" viewBox="0 0 24 24" aria-hidden="true">
          <path d="M12 1a8 8 0 0 0-8 8c0 6 8 14 8 14s8-8 8-14a8 8 0 0 0-8-8zm0 11.5A3.5 3.5 0 1 1 12 5.5a3.5 3.5 0 0 1 0 7z"/>
        </svg>
        <span>ABN 51 718 294 605</span>
      </li>
      <li class="contact-item">
        <svg class="contact-icon" viewBox="0 0 24 24" aria-hidden="true">
          <path d="M12 2 1 12h3v10h6v-6h4v6h6V12h3z"/>
        </svg>
        <span>p.o.box 42 wendouree 3355</span>
      </li>
      <li class="contact-item">
        <svg class="contact-icon" viewBox="0 0 24 24" aria-hidden="true">
          <path d="M1 5h22v14H1zm2 2v.5l9 6 9-6V7l-9 6z"/>
        </svg>
        <span>harbourlinelinings@examplemail.com</span>
      </li>
    </ul>
  </article>
</main>
</body>
</html>
```